BRICKWORK BLUEPRINT: THE RELIABLE WAY TO EARN HUGE GAINS FROM BUDGET HOME UPGRADES

I am looking for a book cover design for my new E-Book.

My idea for the design is a pin board with before and after photos of our properties pinned on it (example attached). I have also attached some photos to use.

PLEASE SUBMIT OTHER DESIGNS ALSO AS THIS WAS JUST AN IDEA BUT I AM OPEN TO OTHER IDEAS ALSO.

Page size is 5x7 inches

Font styles to use
Serif
Sans Serif

Colors
0255a3
3176b5
85acd3
85cae6
33a6d7
0392cd
9bcb3c
abd036
ec1f27

```html
<!DOCTYPE html>
<html lang="en">
<head>
<meta charset="utf-8">
<title>Brickwork Blueprint – E-Book Cover</title>
<link rel="stylesheet" href="https://fonts.googleapis.com/css2?family=Josefin+Sans:wght@300;600&family=Noticia+Text:ital,wght@0,400;0,700;1,400&display=swap">
<style>
  :root {
    --sky-light: #7dbbe2;
    --sky-mid: #5ea6d6;
    --sky-deep: #3f8fc5;
    --ink: #1b1f24;
    --paper: #ffffff;
    --lawn: #5f9a45;
    --lawn-dark: #3f6e32;
    --sky-photo: #8fc3e6;
    --house-grey: #9aa3ad;
  }
  * { margin: 0; padding: 0; box-sizing: border-box; }
  html, body { width: 923px; height: 1200px; overflow: hidden; }
  body { background: var(--sky-deep); }
  .cover {
    position: relative;
    width: 923px; height: 1200px;
    overflow: hidden;
    background: radial-gradient(ellipse at 50% 45%, var(--sky-light) 0%, var(--sky-mid) 55%, var(--sky-deep) 100%);
  }
  .author {
    position: absolute; top: 72px; left: 0; width: 100%;
    text-align: center;
    font-family: "Josefin Sans", sans-serif; font-weight: 300;
    font-size: 33px; letter-spacing: 0.5em; text-indent: 0.5em;
    color: var(--ink);
  }
  .title-art { position: absolute; left: 0; top: 110px; width: 923px; height: 170px; }
  .title-main { font-family: "Noticia Text", serif; font-weight: 400; fill: var(--paper); }
  .title-sub { font-family: "Noticia Text", serif; font-style: italic; fill: var(--paper); }
  .board-line { position: absolute; background: var(--paper); border-radius: 3px; }
  .board-line.vertical { left: 146px; top: 325px; width: 6px; height: 571px; }
  .board-line.horizontal { left: 146px; top: 890px; width: 632px; height: 6px; }
  .connector { position: absolute; height: 5px; background: var(--paper); transform-origin: left center; }
  .photo {
    position: absolute;
    background: var(--paper);
    padding: 5px;
    box-shadow: 0 3px 8px rgba(0,0,0,0.3);
  }
  .photo-fill {
    position: relative; width: 100%; height: 100%;
    background: linear-gradient(180deg, var(--sky-photo) 0%, var(--sky-photo) 28%, var(--house-grey) 29%, var(--house-grey) 58%, var(--lawn) 60%, var(--lawn-dark) 100%);
  }
  .photo-fill.shaded {
    background: linear-gradient(180deg, #a8c6cf 0%, #6f8a6a 35%, #8c8f86 60%, #4f5a48 100%);
  }
  .photo-label {
    position: absolute; bottom: 8px; left: 0; width: 100%;
    text-align: center;
    font-family: "Josefin Sans", sans-serif; font-weight: 600;
    font-size: 17px; letter-spacing: 0.22em;
    color: var(--paper);
    text-shadow: 0 1px 2px rgba(0,0,0,0.5);
  }
  .photo.before-carport { left: 98px; top: 480px; width: 279px; height: 150px; transform: rotate(-3deg); z-index: 1; }
  .photo.after-garden { left: 229px; top: 313px; width: 283px; height: 188px; transform: rotate(1.5deg); z-index: 2; }
  .photo.after-highset { left: 560px; top: 290px; width: 303px; height: 200px; transform: rotate(2deg); z-index: 1; }
  .photo.before-highset { left: 529px; top: 428px; width: 212px; height: 132px; transform: rotate(0.5deg); z-index: 2; }
  .photo.after-cottage { left: 427px; top: 572px; width: 413px; height: 275px; transform: rotate(-1deg); z-index: 1; }
  .photo.before-cottage { left: 178px; top: 722px; width: 230px; height: 150px; transform: rotate(-2.5deg); z-index: 2; }
  .photo.after-cottage .photo-label, .photo.after-highset .photo-label { font-size: 19px; }
  .after-highset .photo-label { text-align: right; padding-right: 12px; }
  .subtitle {
    position: absolute; top: 958px; left: 0; width: 100%;
    text-align: center;
    font-family: "Noticia Text", serif; font-weight: 700;
    font-size: 37px; line-height: 1.17; letter-spacing: 0.03em;
    color: var(--paper);
  }
  .imprint {
    position: absolute; top: 1153px; left: 0; width: 100%;
    text-align: center;
    font-family: "Josefin Sans", sans-serif; font-weight: 300;
    font-size: 19px; letter-spacing: 0.22em;
    color: var(--paper);
  }
</style>
</head>
<body>
<main class="cover">
  <p class="author">MARCUS ELLERY</p>

  <svg class="title-art" viewBox="0 0 923 170" aria-label="Brickwork Blueprint">
    <text class="title-main" x="69" y="96" font-size="112" textLength="796" lengthAdjust="spacingAndGlyphs">BRICKWORK</text>
    <text class="title-sub" x="222" y="155" font-size="58" textLength="478" lengthAdjust="spacing">BLUEPRINT</text>
  </svg>

  <div class="board-line vertical"></div>
  <div class="board-line horizontal"></div>
  <div class="connector" style="left:640px; top:560px; width:22px; transform:rotate(-55deg);"></div>
  <div class="connector" style="left:404px; top:835px; width:30px; transform:rotate(-35deg);"></div>

  <figure class="photo before-carport">
    <div class="photo-fill shaded" role="img" aria-label="Overgrown yard and carport before renovation">
      <span class="photo-label">BEFORE</span>
    </div>
  </figure>
  <figure class="photo after-garden">
    <div class="photo-fill" role="img" aria-label="Renovated house with green lawn and stepping stones under large trees">
      <span class="photo-label">AFTER</span>
    </div>
  </figure>
  <figure class="photo after-highset">
    <div class="photo-fill" role="img" aria-label="Renovated two-storey house painted blue-grey with dark garage doors">
      <span class="photo-label">AFTER</span>
    </div>
  </figure>
  <figure class="photo before-highset">
    <div class="photo-fill shaded" role="img" aria-label="Two-storey house before renovation with concrete driveway">
      <span class="photo-label">BEFORE</span>
    </div>
  </figure>
  <figure class="photo after-cottage">
    <div class="photo-fill" role="img" aria-label="Renovated grey cottage with white veranda and fresh lawn">
      <span class="photo-label">AFTER</span>
    </div>
  </figure>
  <figure class="photo before-cottage">
    <div class="photo-fill shaded" role="img" aria-label="Cottage with tiled roof before renovation">
      <span class="photo-label">BEFORE</span>
    </div>
  </figure>

  <h2 class="subtitle">THE RELIABLE WAY TO EARN<br>HUGE GAINS FROM BUDGET<br>HOME UPGRADES</h2>

  <p class="imprint">ELLERY HOMES • BUILD IT BETTER</p>
</main>
</body>
</html>
```